Design a Bold Tradeshow Backdrop for a Sustainable Cleaning Technology

We need a professional, high-impact 10' × 8' tradeshow backdrop for Vornelle®, a commercial cleaning technology company. 143.75" x 90" high and needs bleeds in the 143.75" direction for printing but the graphic area is 10' wide.

Our first event will have an audience that includes K–12 school administrators, facility managers, business officials, and custodial decision-makers. However, this backdrop will be used at multiple future trade shows across different commercial and institutional markets.

The design therefore needs to be universal rather than specifically education- or school-themed.

Our goal is to stop attendees as they walk past the booth and immediately communicate a simple message:

Safer and more sustainable cleaning can also cost substantially less than conventional cleaning chemicals.

We want the design to feel modern, innovative, clean, sustainable, credible, commercial, and premium. It should resonate with K–12 decision-makers while being equally appropriate at events serving commercial facilities, healthcare, hospitality, government, property management, transportation, and other institutional markets.

It should NOT look like a traditional janitorial supply advertisement and should not be overly busy.

The most important messages need to be understandable from approximately 10–20 feet away.

Required Messaging

The primary headline should be:

SUSTAINABLE CLEANING
DOES NOT HAVE TO BE EXPENSIVE.

Three major value propositions should be prominently displayed:

FREE
Cleaning Chemical Analysis
See how much you can save.

SAVE UP TO 60% or More
on Cleaning Chemical Costs

AS LITTLE AS $0.27/GALLON

We would also like a strong secondary message incorporated into the design:

SMARTER CLEANING.
High Performance. Low Cost. Safer.

Visual Direction — Important

Rather than showing a K–12 school hallway or other environment that limits the backdrop to the education market, we want a sophisticated, universal commercial or institutional environment.

This could be a bright, contemporary commercial facility, lobby, corridor, office environment, public building, or other premium architectural space that could reasonably represent many different types of facilities.

The environment should communicate:

Cleanliness • Safety • Sustainability • Professionalism • Efficiency • High Performance

We want someone from a school, hospital, hotel, office building, airport, government facility, or other commercial property to be able to look at the backdrop and relate the imagery to their own facility.

Please avoid imagery that makes the backdrop industry-specific.

We also want to avoid clichéd environmental imagery. The design does not need to be covered in leaves, trees, water droplets, recycling symbols, or other obvious "green" graphics to communicate sustainability. We prefer a sophisticated commercial interpretation of sustainability.

Color & Brand Direction

We want the overall color palette to stay primarily within:

Blues — consistent with our corporate identity

Greens — to reinforce sustainability, safety, efficiency, and environmental responsibility

White — strongly encouraged for clean space, contrast, and an open contemporary appearance

Black — should be limited primarily to text where necessary for readability

Please avoid making black a major background or dominant design color.

We want the finished display to have a bright, clean, sophisticated, sustainable look and feel rather than a dark or industrial appearance.

The design should use significant negative space and a strong visual hierarchy.

Less is more.

We prefer a few large, powerful messages that can be understood quickly rather than numerous small bullet points, paragraphs, or icons.

Creative Freedom

The attached concept image is provided to communicate our general direction and messaging only.

It does not need to be copied.

We are specifically running this contest because we want designers to improve upon our initial concept and show us different creative approaches to presenting the Vornelle value proposition.

We are open to creative interpretations of the commercial environment, composition, typography, use of negative space, and how the three major financial benefits are presented.

The finished design should feel like an innovative commercial technology brand, not simply another cleaning chemical company.

Corporate Logo — Very Important

We are attaching our official Vornelle® corporate logo for use in the design.

DO NOT redraw, recreate, modify, stylize, reinterpret, trace, or AI-generate the Vornelle logo.

The supplied corporate logo must be inserted directly into the artwork exactly as provided, maintaining its original proportions, colors, typography, trademark elements, and graphic design.

The logo should generally appear in the upper-left area of the backdrop but should not overwhelm the primary marketing message.

Printer Template & Graphic Sizing

We are also attaching the printer's official graphic template and instructions for the 8' × 8' tension-fabric display.

Designers should create their artwork using these supplied specifications so the winning design can be transferred directly into production.

The printer requires that the original document size not be changed, artwork be created on the designated design layer or a new layer, images be embedded, text be converted to outlines, and the finished production artwork be supplied as a PDF.

Please pay particular attention to the bleed area, finished size, and safe artwork area when positioning important text, graphics, and the corporate logo.

Physical Booth Context

The backdrop will sit behind an 8' tradeshow table.

The complete booth will also contain:

A blue stretch tablecloth with the Vornelle corporate logo
BrevoMax and Vornelle product containers and samples on the table
An HulaDrent chemical mixing/dilution station displayed on an elevated stand to the left
A television/monitor to the right demonstrating our online ROI cost-savings calculator

Because these other booth elements will explain our products and technology in greater detail, the backdrop should NOT attempt to explain everything we do.

Its primary purpose is to stop traffic, establish the Vornelle brand, and communicate our core economic and sustainability value proposition.

Final Deliverables

The winning designer must provide artwork properly sized and positioned using our supplied 8' × 8' tension-fabric display template.

Final files should include:

Print-ready, high-resolution PDF
Editable source/vector artwork
All images embedded
Fonts converted to outlines
Artwork correctly positioned within the supplied printer template
Original Vornelle corporate logo incorporated without modification
The 3–5 Second Test

This is perhaps the most important requirement.

Someone walking down a tradeshow aisle should be able to look at the backdrop for 3–5 seconds and understand:

Vornelle offers safer, sustainable, high-performance commercial cleaning — at a lower cost.

The three offers we particularly want them to remember are:

FREE CHEMICAL ANALYSIS

SAVE UP TO 60%

AS LITTLE AS $0.27/GALLON

The overall takeaway should be:

Sustainable cleaning does not have to cost more.

We want the winning design to make that message immediately understandable, credible, and memorable.

Colors
0054AA
0677BA
7BADD7
CADEEF
E8F1F8
0094D4
00A9DD
6FCCEA
C7EBF8
E9F6FB
00AB8E
00BBA5
67D7C9
C6EFE9
E9F9F6
59FF00
82FF00
B8FF75
E3FFCB
F4FFEA

```html
<!DOCTYPE html>
<html lang="en">
<head>
<meta charset="utf-8">
<title>Vornelle – Sustainable Cleaning Backdrop</title>
<link href="https://fonts.googleapis.com/css2?family=Poppins:wght@400;500;600;700;800&display=swap" rel="stylesheet">
<style>
  :root {
    --navy: #1b3a6b;
    --navy-deep: #0d1f5c;
    --headline-green: #72a83c;
    --bar-green: #97cd4f;
    --accent-blue: #0677ba;
    --ink: #1a1a1a;
    --white: #ffffff;
  }
  html, body {
    margin: 0;
    padding: 0;
    width: 1200px;
    height: 1200px;
    overflow: hidden;
    background: var(--white);
  }
  .backdrop {
    display: block;
    width: 1200px;
    height: 1200px;
    font-family: "Poppins", sans-serif;
  }
  .brand-name { font-weight: 700; fill: var(--navy); }
  .headline { font-weight: 700; }
  .headline .green { fill: var(--headline-green); }
  .headline .navy { fill: var(--navy); }
  .offer-big { font-weight: 800; fill: var(--navy); }
  .offer-small { font-weight: 800; fill: var(--navy); }
  .offer-copy { font-weight: 400; fill: var(--ink); font-size: 19px; }
  .offer-label { font-weight: 400; fill: var(--navy); font-size: 18px; }
  .step-num { font-weight: 700; fill: var(--white); font-size: 24px; }
  .smarter { font-weight: 800; fill: var(--white); }
  .bar-text { font-weight: 400; fill: var(--ink); font-size: 20px; }
  .benefit { font-weight: 700; fill: var(--white); font-size: 30px; }
</style>
</head>
<body>
<svg class="backdrop" viewBox="0 0 1200 1200" xmlns="http://www.w3.org/2000/svg">
  <defs>
    <linearGradient id="stripeGrad" x1="0" y1="0" x2="0" y2="1">
      <stop offset="0" stop-color="#0d1f5c"/>
      <stop offset="0.35" stop-color="#1e3f72"/>
      <stop offset="0.7" stop-color="#8cc84b"/>
      <stop offset="1" stop-color="#0677ba"/>
    </linearGradient>
    <linearGradient id="interiorGrad" x1="0" y1="0" x2="0.3" y2="1">
      <stop offset="0" stop-color="#e9ddd0"/>
      <stop offset="0.25" stop-color="#c9a78a"/>
      <stop offset="0.45" stop-color="#f3ece4"/>
      <stop offset="0.7" stop-color="#d8c2ad"/>
      <stop offset="1" stop-color="#b8977c"/>
    </linearGradient>
    <linearGradient id="panelGrad" x1="0" y1="0" x2="1" y2="0">
      <stop offset="0" stop-color="#8dc84a"/>
      <stop offset="0.45" stop-color="#3f6b6c"/>
      <stop offset="1" stop-color="#1d3566"/>
    </linearGradient>
    <linearGradient id="navyBand" x1="0" y1="0" x2="1" y2="1">
      <stop offset="0" stop-color="#123680"/>
      <stop offset="1" stop-color="#0a0f4a"/>
    </linearGradient>
    <radialGradient id="stepGrad" cx="0.3" cy="0.7" r="0.9">
      <stop offset="0" stop-color="#6fb043"/>
      <stop offset="1" stop-color="#1b3a6b"/>
    </radialGradient>
    <filter id="softShadow" x="-10%" y="-10%" width="120%" height="120%">
      <feDropShadow dx="0" dy="0" stdDeviation="5" flood-color="#000" flood-opacity="0.18"/>
    </filter>
  </defs>

  <!-- Diagonal accent stripe and facility imagery -->
  <polygon class="accent-stripe" points="554,0 700,0 921,902 902,902" fill="url(#stripeGrad)"/>
  <path class="facility-image" role="img" aria-label="Bright marble-floored commercial lobby with columns, plants and tall windows"
        d="M690 0 Q625 110 650 200 L921 902 L1200 902 L1200 0 Z" fill="url(#interiorGrad)"/>

  <!-- Brand name -->
  <g class="brand">
    <text class="brand-name" x="70" y="200" font-size="84">Vornelle®</text>
  </g>

  <!-- Headline -->
  <g class="headline" font-size="82">
    <text class="green" x="74" y="387" textLength="519" lengthAdjust="spacingAndGlyphs">SUSTAINABLE</text>
    <text class="navy" x="74" y="459" textLength="392" lengthAdjust="spacingAndGlyphs">CLEANING</text>
    <text class="green" x="74" y="531" textLength="614" lengthAdjust="spacingAndGlyphs">DOES NOT HAVE</text>
    <text class="navy" x="74" y="603" textLength="669" lengthAdjust="spacingAndGlyphs">TO BE EXPENSIVE.</text>
  </g>

  <!-- Middle offer card (behind step markers) -->
  <rect class="offer-card" x="308" y="717" width="291" height="172" fill="#fff" filter="url(#softShadow)"/>
  <rect x="300" y="700" width="307" height="16" fill="#fff"/>
  <rect x="300" y="889" width="307" height="13" fill="#fff"/>

  <!-- Step markers -->
  <g class="steps">
    <line x1="194" y1="686" x2="413" y2="686" stroke="var(--navy)" stroke-width="2" stroke-dasharray="2 3"/>
    <line x1="482" y1="686" x2="687" y2="686" stroke="var(--navy)" stroke-width="2" stroke-dasharray="2 3"/>
    <g>
      <circle cx="158" cy="686" r="21" fill="url(#stepGrad)" stroke="var(--navy)" stroke-width="1.5"/>
      <circle cx="158" cy="686" r="17" fill="none" stroke="#fff" stroke-width="1.5"/>
      <text class="step-num" x="158" y="695" text-anchor="middle">1</text>
    </g>
    <g>
      <circle cx="448" cy="686" r="21" fill="url(#stepGrad)" stroke="var(--navy)" stroke-width="1.5"/>
      <circle cx="448" cy="686" r="17" fill="none" stroke="#fff" stroke-width="1.5"/>
      <text class="step-num" x="448" y="695" text-anchor="middle">2</text>
    </g>
    <g>
      <circle cx="720" cy="686" r="21" fill="url(#stepGrad)" stroke="var(--navy)" stroke-width="1.5"/>
      <circle cx="720" cy="686" r="17" fill="none" stroke="#fff" stroke-width="1.5"/>
      <text class="step-num" x="720" y="695" text-anchor="middle">3</text>
    </g>
  </g>

  <!-- Offers -->
  <g class="offer offer-free">
    <text class="offer-big" x="162" y="789" font-size="64" text-anchor="middle" textLength="144" lengthAdjust="spacingAndGlyphs">FREE</text>
    <text class="offer-copy" x="162" y="824" text-anchor="middle">Cleaning Chemical</text>
    <text class="offer-copy" x="162" y="848" text-anchor="middle">Analysis See how</text>
    <text class="offer-copy" x="162" y="872" text-anchor="middle">much you can save.</text>
  </g>

  <g class="offer offer-save">
    <text class="offer-small" x="345" y="764" font-size="27" textLength="72" lengthAdjust="spacingAndGlyphs">SAVE</text>
    <text class="offer-small" x="343" y="789" font-size="27" textLength="80" lengthAdjust="spacingAndGlyphs">UP TO</text>
    <text class="offer-big" x="430" y="789" font-size="66" textLength="135" lengthAdjust="spacingAndGlyphs">60%</text>
    <text class="offer-copy" x="451" y="829" text-anchor="middle">or More on Cleaning</text>
    <text class="offer-copy" x="451" y="853" text-anchor="middle">Chemical Costs</text>
  </g>

  <g class="offer offer-price">
    <text class="offer-label" x="722" y="755" text-anchor="middle">AS LITTLE AS</text>
    <text class="offer-big" x="645" y="824" font-size="66" textLength="153" lengthAdjust="spacingAndGlyphs"><tspan font-size="30" dy="-28">$</tspan><tspan dy="28">0.27</tspan></text>
    <text class="offer-label" x="722" y="861" text-anchor="middle">/GALLON</text>
  </g>

  <!-- Bottom band -->
  <rect class="band-navy" x="0" y="916" width="1200" height="284" fill="url(#navyBand)"/>
  <path class="band-panel" d="M421 916 L1200 916 L1200 1200 L471 1200 L392 990 Q386 975 395 962 Z"
        fill="url(#panelGrad)" stroke="#fff" stroke-width="3"/>

  <g class="smarter-block">
    <text class="smarter" x="69" y="987" font-size="56" textLength="256" lengthAdjust="spacingAndGlyphs">SMARTER</text>
    <text class="smarter" x="69" y="1039" font-size="56" textLength="294" lengthAdjust="spacingAndGlyphs">CLEANING.</text>
    <polygon points="65,1071 356,1071 364,1099 65,1099" fill="var(--bar-green)"/>
    <polygon points="65,1105 356,1105 364,1133 65,1133" fill="var(--white)"/>
    <polygon points="65,1139 356,1139 364,1167 65,1167" fill="var(--bar-green)"/>
    <text class="bar-text" x="79" y="1093">High Performance.</text>
    <text class="bar-text" x="79" y="1127">Low Cost.</text>
    <text class="bar-text" x="79" y="1161">Safer.</text>
  </g>

  <g class="benefits">
    <line x1="763" y1="965" x2="763" y2="1135" stroke="#fff" stroke-opacity="0.6" stroke-width="1.5"/>
    <g class="check">
      <circle cx="472" cy="994" r="11" fill="#fff"/>
      <polyline points="466,994 470,998 478,989" fill="none" stroke="#5f8f4a" stroke-width="2.5" stroke-linecap="round" stroke-linejoin="round"/>
      <circle cx="472" cy="1049" r="11" fill="#fff"/>
      <polyline points="466,1049 470,1053 478,1044" fill="none" stroke="#5f8f4a" stroke-width="2.5" stroke-linecap="round" stroke-linejoin="round"/>
      <circle cx="472" cy="1103" r="11" fill="#fff"/>
      <polyline points="466,1103 470,1107 478,1098" fill="none" stroke="#5f8f4a" stroke-width="2.5" stroke-linecap="round" stroke-linejoin="round"/>
      <circle cx="817" cy="993" r="11" fill="#fff"/>
      <polyline points="811,993 815,997 823,988" fill="none" stroke="var(--navy)" stroke-width="2.5" stroke-linecap="round" stroke-linejoin="round"/>
      <circle cx="817" cy="1048" r="11" fill="#fff"/>
      <polyline points="811,1048 815,1052 823,1043" fill="none" stroke="var(--navy)" stroke-width="2.5" stroke-linecap="round" stroke-linejoin="round"/>
      <circle cx="817" cy="1102" r="11" fill="#fff"/>
      <polyline points="811,1102 815,1106 823,1097" fill="none" stroke="var(--navy)" stroke-width="2.5" stroke-linecap="round" stroke-linejoin="round"/>
    </g>
    <text class="benefit" x="497" y="1005" textLength="197" lengthAdjust="spacingAndGlyphs">Cleanliness</text>
    <text class="benefit" x="497" y="1060">Safety</text>
    <text class="benefit" x="497" y="1114" textLength="237" lengthAdjust="spacingAndGlyphs">Sustainability</text>
    <text class="benefit" x="847" y="1004" textLength="273" lengthAdjust="spacingAndGlyphs">Professionalism</text>
    <text class="benefit" x="847" y="1059" textLength="163" lengthAdjust="spacingAndGlyphs">Efficiency</text>
    <text class="benefit" x="847" y="1113" textLength="307" lengthAdjust="spacingAndGlyphs">High Performance</text>
  </g>
</svg>
</body>
</html>
```